Business card design for my trucking company

I would like a business card designed for my new trucking company. Please use my logo. the rest of the design is up to you. i would like my clients to say wow when they see the card. Im looking forward to seeing your designs

Target Market(s)

Industry/Entity Type

Trucking Company

Contact Information for Business Card

Marcus Tillbrook President
518-364-7120
ridgelinehaulage@examplemail.net

Font styles to use
Serif

Requirements
Must have
• my logo, name and number. we are located in Schenectady New York. the rest is up to you
Nice to have
• up to you
Should not have
• none

```html
<!DOCTYPE html>
<html lang="en">
<head>
<meta charset="utf-8">
<title>Ridgeline Haulage &amp; Logistics Inc. — Business Card</title>
<link rel="stylesheet" href="https://fonts.googleapis.com/css2?family=Archivo:wght@800&family=PT+Serif&display=swap">
<style>
  :root {
    --stage: #2b2b2c;
    --card-dark: #1d1d1e;
    --card-light: #ffffff;
    --brand-red: #e3202a;
    --ink-grey: #5c5c5c;
    --mark-grey: #6e6e70;
    --sans: "Archivo", "Arial Black", sans-serif;
    --serif: "PT Serif", "Times New Roman", serif;
  }
  * { box-sizing: border-box; margin: 0; padding: 0; }
  html, body { width: 1200px; height: 895px; overflow: hidden; }
  body {
    background: var(--stage);
    display: flex;
    flex-direction: column;
    align-items: center;
    justify-content: center;
    gap: 44px;
  }
  .card {
    position: relative;
    width: 620px;
    height: 354px;
    overflow: hidden;
    box-shadow: 0 10px 28px rgba(0,0,0,.45);
  }
  .card::after {
    content: "";
    position: absolute;
    left: 0; right: 0; bottom: 0;
    height: 7px;
    background: var(--brand-red);
  }
  .card--back { background: var(--card-dark); }
  .card--front { background: var(--card-light); }

  .wordmark {
    position: absolute;
    font-family: var(--sans);
    font-weight: 800;
    text-transform: uppercase;
    line-height: 1;
  }
  .wordmark__main { display: block; letter-spacing: 1px; }
  .wordmark__sub { display: block; letter-spacing: 2.2px; margin-top: 6px; }

  .card--back .wordmark {
    color: var(--mark-grey);
    left: 50%; top: 50%;
    transform: translate(-50%, -54%);
    text-align: left;
  }
  .card--back .wordmark__main { font-size: 56px; }
  .card--back .wordmark__sub { font-size: 17.5px; }

  .card--front .wordmark {
    color: var(--brand-red);
    right: 38px; top: 58px;
  }
  .card--front .wordmark__main { font-size: 44px; }
  .card--front .wordmark__sub { font-size: 13.7px; }

  .contact {
    position: absolute;
    left: 40px; bottom: 40px;
  }
  .contact__name {
    font-family: var(--sans);
    font-weight: 800;
    font-size: 23px;
    color: var(--brand-red);
    text-transform: uppercase;
    letter-spacing: .3px;
  }
  .contact__role {
    font-family: var(--serif);
    font-size: 16px;
    color: var(--ink-grey);
    margin-top: 2px;
  }
  .contact__list { list-style: none; margin-top: 16px; }
  .contact__item {
    display: flex;
    align-items: center;
    gap: 12px;
    font-family: var(--serif);
    font-size: 16px;
    color: var(--ink-grey);
    line-height: 1.45;
  }
  .contact__icon { width: 14px; height: 14px; flex: none; }
</style>
</head>
<body>
  <section class="card card--back" aria-label="Card back">
    <div class="wordmark">
      <span class="wordmark__main">Ridgeline</span>
      <span class="wordmark__sub">Haulage &amp; Logistics Inc.</span>
    </div>
  </section>

  <section class="card card--front" aria-label="Card front">
    <div class="wordmark">
      <span class="wordmark__main">Ridgeline</span>
      <span class="wordmark__sub">Haulage &amp; Logistics Inc.</span>
    </div>

    <div class="contact">
      <h1 class="contact__name">Marcus Tillbrook</h1>
      <p class="contact__role">President</p>
      <ul class="contact__list">
        <li class="contact__item">
          <svg class="contact__icon" viewBox="0 0 24 24" aria-hidden="true">
            <path fill="#e3202a" d="M6.6 10.8a15.1 15.1 0 0 0 6.6 6.6l2.2-2.2a1 1 0 0 1 1-.25 11.4 11.4 0 0 0 3.6.57 1 1 0 0 1 1 1V20a1 1 0 0 1-1 1A17 17 0 0 1 3 4a1 1 0 0 1 1-1h3.5a1 1 0 0 1 1 1c0 1.25.2 2.45.57 3.57a1 1 0 0 1-.25 1z"/>
          </svg>
          518-364-7120
        </li>
        <li class="contact__item">
          <svg class="contact__icon" viewBox="0 0 24 24" aria-hidden="true">
            <rect x="2.5" y="5" width="19" height="14" rx="1.5" fill="none" stroke="#e3202a" stroke-width="2"/>
            <path d="M3 6l9 7 9-7" fill="none" stroke="#e3202a" stroke-width="2"/>
          </svg>
          ridgelinehaulage@examplemail.net
        </li>
      </ul>
    </div>
  </section>
</body>
</html>
```